looking to have a web site for the company which provides services in the industrial and commercial sectors such as: electrical, automation control and system integration, construction and maintenance, millwright, equipment assembly repair and installation. I have the domain already brivanholdings.net and logo. Most recent projects fulfilled for the following clients: MarlowKibbleCo, Dunholt University, OKSU, FALSTO, Tazzik, Prairie Grains

Target Market(s)

industrial and commercial sectors in electrical, automation, millwright and fabrication fields

Industry/Entity Type

Industrial

Coding

Coded - Design and coding required

Number of Pages Required

5+ page

Font styles to use
Sans Serif

Colors

Designer to choose colors to be used in the design.

Requirements
Nice to have
• looking to get something not complicated, nicely presented with minimum or no scrolling

```html
<!DOCTYPE html>
<html lang="en">
<head>
<meta charset="utf-8">
<title>Brivan Group Ltd — Industrial &amp; Commercial Services</title>
<link href="https://fonts.googleapis.com/css2?family=Lato:ital,wght@0,300;0,400;0,700;0,900;1,400&display=swap" rel="stylesheet">
<style>
:root{
  --blue:#1a9ad6;
  --blue-dark:#1683b8;
  --ink:#222a30;
  --text:#5b6268;
  --muted:#9aa1a6;
  --line:#e3e6e9;
  --soft:#eef1f4;
  --white:#ffffff;
  --footer:#454749;
  --footer-bar:#353739;
}
*{box-sizing:border-box;margin:0;padding:0}
html,body{width:1200px;height:3614px;overflow:hidden}
body{font-family:"Lato",Arial,sans-serif;color:var(--text);background:var(--white);position:relative}
.wrap{width:940px;margin:0 auto;position:relative}
a{color:inherit;text-decoration:none}
.btn{display:inline-block;background:var(--blue);color:var(--white);font-size:12px;font-weight:700;letter-spacing:.5px;padding:14px 26px;text-transform:uppercase}
.btn-ghost{display:inline-block;border:1px solid rgba(255,255,255,.85);color:var(--white);font-size:12px;font-weight:700;padding:12px 22px}

/* header */
.site-header{height:97px;position:relative}
.brand{position:absolute;left:0;top:26px;line-height:1}
.brand-name{font-size:30px;font-weight:900;color:var(--blue);letter-spacing:-.5px;display:block}
.brand-sub{font-size:11px;font-weight:700;color:var(--muted);letter-spacing:5px;display:block;margin-top:2px}
.topbar{position:absolute;right:0;top:16px;display:flex;align-items:center;gap:12px}
.social{display:flex;gap:10px}
.social span{width:12px;height:12px;border-radius:50%;background:#b5babe;display:block}
.phone{display:flex;align-items:center;gap:6px;font-size:21px;font-weight:700;color:var(--ink)}
.main-nav{position:absolute;right:0;top:62px;display:flex;gap:24px;font-size:12px;text-transform:uppercase;color:#4a5156}
.main-nav a{padding-bottom:9px}
.main-nav a.active{color:var(--blue);border-bottom:2px solid var(--blue)}

/* hero */
.hero{height:620px;position:relative;background:linear-gradient(90deg,#c9cfd4 0%,#b7bec4 40%,#9aa2a8 70%,#b5bbc0 100%)}
.hero-copy{position:absolute;left:140px;top:220px}
.hero-kicker{font-style:italic;color:var(--blue);font-size:20px;margin-bottom:12px}
.hero-title{font-size:36px;font-weight:900;color:var(--ink);line-height:1.15;margin-bottom:24px;text-transform:uppercase}
.dots{position:absolute;left:50%;bottom:16px;transform:translateX(-50%);display:flex;gap:6px}
.dots span{width:9px;height:9px;border-radius:50%;background:var(--white);display:block}
.dots span.on{background:#556;}

/* sectors */
.sectors{height:733px;position:relative}
.sectors-copy{position:absolute;left:140px;top:112px;width:460px}
.kicker{color:var(--blue);font-size:13px;margin-bottom:12px}
.sec-title{font-size:24px;font-weight:900;color:var(--ink);line-height:1.2;text-transform:uppercase;margin-bottom:18px}
.body-text{font-size:13px;line-height:2;color:var(--text)}
.features{display:flex;gap:36px;margin:26px 0 32px}
.features li{list-style:none;font-size:11px;font-weight:900;color:var(--ink);line-height:1.3;text-transform:uppercase;width:120px}
.shot{position:absolute;box-shadow:0 4px 14px rgba(0,0,0,.18);border:6px solid var(--white)}
.s1{left:657px;top:195px;width:190px;height:192px;background:linear-gradient(135deg,#a9b1b6,#d7a64a 55%,#6e7b86)}
.s2{left:864px;top:99px;width:194px;height:194px;background:linear-gradient(135deg,#8f979c,#c8ced3)}
.s3{left:864px;top:309px;width:194px;height:194px;background:linear-gradient(135deg,#c0c6cb,#516a8a 60%,#9aa2a8)}
.s4{left:657px;top:401px;width:190px;height:194px;background:linear-gradient(135deg,#9ca3a8,#6f777c)}

/* services */
.services{display:flex;height:482px}
.service{flex:1;position:relative;display:flex;flex-direction:column;align-items:center;justify-content:center;text-align:center;color:var(--white);padding:0 40px}
.service::after{content:"";position:absolute;inset:0;background:rgba(25,30,35,.45)}
.service>*{position:relative;z-index:1}
.sv1{background:linear-gradient(135deg,#8b6a5a,#5e6a76)}
.sv2{background:linear-gradient(135deg,#4f6a55,#7a8d74)}
.sv3{background:linear-gradient(135deg,#6a6d70,#4b5055)}
.service h3{font-size:19px;font-weight:900;text-transform:uppercase;margin:0 0 10px;padding-top:20px}
.service p{font-size:13px;line-height:1.6;margin-bottom:32px}

/* news */
.news{height:518px;position:relative}
.news-copy{position:absolute;left:140px;top:100px;width:260px}
.news-copy .sec-title{margin-bottom:14px}
.news-copy .body-text{font-size:12px;line-height:1.9;height:115px;overflow:hidden;margin-bottom:26px}
.card{position:absolute;top:122px;width:290px}
.c1{left:454px}.c2{left:768px}
.card-img{height:192px}
.c1 .card-img{background:linear-gradient(135deg,#7d868c,#b4babe 50%,#5c646a)}
.c2 .card-img{background:linear-gradient(135deg,#6d767c,#c7ccd0 50%,#4f575d)}
.card h4{color:var(--blue);font-size:11px;font-weight:700;text-transform:uppercase;margin:20px 0 4px}
.card time{font-size:11px;color:var(--muted);display:block;margin-bottom:6px}
.card .more{font-size:10px;font-weight:900;color:var(--ink);text-transform:uppercase}

/* about */
.about{height:550px;background:var(--soft);text-align:center;padding-top:80px}
.about .kicker{font-size:15px;margin-bottom:14px}
.about h2{font-size:25px;font-weight:900;color:var(--ink);text-transform:uppercase;margin-bottom:22px}
.about .lead{font-size:12px;line-height:1.9;color:#4a5156;margin-bottom:34px}
.pillars{display:flex;justify-content:space-between;width:800px;margin:0 auto 36px}
.pillar{width:210px}
.pillar svg{display:block;margin:0 auto 14px}
.pillar h5{font-size:12px;font-weight:700;color:var(--ink);text-transform:uppercase;margin-bottom:12px}
.pillar p{font-size:11px;line-height:1.8;color:var(--muted)}

/* clients */
.clients{height:314px;text-align:center;padding-top:48px}
.clients h2{font-size:23px;font-weight:900;color:var(--ink);text-transform:uppercase;margin-bottom:18px}
.clients .lead{font-size:12px;line-height:1.9;width:700px;margin:0 auto 28px}
.logos{display:flex;justify-content:space-between;width:940px;margin:0 auto}
.logo{flex:1;height:80px;display:flex;align-items:center;justify-content:center;gap:8px;border-right:1px solid var(--line);font-size:15px;font-weight:700;color:var(--ink)}
.logo:last-child{border-right:0}
.logo i{width:12px;height:12px;background:var(--blue);display:block}

/* footer */
.site-footer{height:300px;background:var(--footer);color:#d6d9dc}
.site-footer .wrap{height:300px}
.foot-brand{position:absolute;left:0;top:42px;line-height:1}
.foot-brand .brand-name{color:var(--white);font-size:26px}
.foot-brand .brand-sub{color:#b8bcbf;font-size:10px}
.foot-social{position:absolute;left:0;top:110px;display:flex;gap:12px}
.foot-social span{width:11px;height:11px;border-radius:50%;background:#9da2a6;display:block}
.foot-links{position:absolute;top:38px;list-style:none;font-size:11px;line-height:2.2;color:var(--white)}
.fl1{left:246px}.fl2{left:430px}
.foot-contact{position:absolute;left:720px;top:42px;font-size:11px;line-height:2;color:var(--white);width:220px}
.foot-bar{position:absolute;left:0;right:0;bottom:18px;height:62px;background:var(--footer-bar);display:flex;align-items:center;justify-content:space-between;padding:0 18px;font-size:10px;color:#c9cdd0}
.foot-bar nav{display:flex;gap:16px}
</style>
</head>
<body>

<header class="site-header wrap">
  <a class="brand" href="#"><span class="brand-name">BRIVAN</span><span class="brand-sub">GROUP LTD</span></a>
  <div class="topbar">
    <div class="social"><span></span><span></span><span></span></div>
    <div class="phone">
      <svg width="16" height="16" viewBox="0 0 24 24" fill="#222a30"><path d="M6.6 10.8a15 15 0 0 0 6.6 6.6l2.2-2.2a1 1 0 0 1 1-.25 11.4 11.4 0 0 0 3.6.57 1 1 0 0 1 1 1V20a1 1 0 0 1-1 1A17 17 0 0 1 3 4a1 1 0 0 1 1-1h3.5a1 1 0 0 1 1 1c0 1.25.2 2.45.57 3.57a1 1 0 0 1-.25 1z"/></svg>
      555 014 2 346
    </div>
  </div>
  <nav class="main-nav">
    <a class="active" href="#">Home</a><a href="#">About Us</a><a href="#">Services</a><a href="#">Utility Fabrication</a><a href="#">Capabilities</a><a href="#">Process Machinery</a><a href="#">News</a><a href="#">Contact</a>
  </nav>
</header>

<section class="hero" role="img" aria-label="Photo of industrial grain silos and a processing tower under a cloudy sky">
  <div class="hero-copy">
    <p class="hero-kicker">We make it easy</p>
    <h1 class="hero-title">For our customers<br>to do business with us!</h1>
    <a class="btn" href="#">Learn More</a>
  </div>
  <div class="dots"><span class="on"></span><span></span><span></span><span></span></div>
</section>

<section class="sectors">
  <div class="sectors-copy">
    <p class="kicker">we've got you and your needs covered</p>
    <h2 class="sec-title">Industrial and<br>commercial sectors</h2>
    <p class="body-text">Brivan Group, doubled in size, along with a growing assortment of high quality machines, cranes, saws, and welders year by year. Now that it's 2016 Brivan Group a completely CNC automated facility capable of fulfilling any aspect of the fabrication process up to 2000 tons per job along with 40 story stair capacity. Brivan Group shop was built in 1987 to accommodate the growth of the company, aiding in Harlan Welding's ability in fabricating increasingly larger jobs and in greater quantity.</p>
    <ul class="features">
      <li>Contrary to popular belief</li>
      <li>Lorem ipsum is simply dummy</li>
      <li>Map lorem ipsum is simply</li>
    </ul>
    <a class="btn" href="#">Learn More</a>
  </div>
  <div class="shot s1" role="img" aria-label="Photo of a worker beside yellow safety railings and blue machinery"></div>
  <div class="shot s2" role="img" aria-label="Photo of wrapped equipment inside a plant"></div>
  <div class="shot s3" role="img" aria-label="Photo of an electrical control cabinet with a blue label"></div>
  <div class="shot s4" role="img" aria-label="Photo of grey electrical enclosures mounted on a wall"></div>
</section>

<section class="services">
  <div class="service sv1" role="img" aria-label="Photo of wired process machinery control panels">
    <h3>Process Machinery</h3>
    <p>Lorem ipsum dolor sit amet, consectetur adipiscing elit. Pellent esque dignissim eros a sapien tempus, ut eleifend neque convallis.</p>
    <a class="btn-ghost" href="#">LEARN MORE</a>
  </div>
  <div class="service sv2" role="img" aria-label="Photo of industrial filter system ducting">
    <h3>Filter Systems</h3>
    <p>Lorem ipsum dolor sit amet, consectetur adipiscing elit. Pellent esque dignissim eros a sapien tempus, ut eleifend neque convallis.</p>
    <a class="btn-ghost" href="#">LEARN MORE</a>
  </div>
  <div class="service sv3" role="img" aria-label="Photo of conveyor equipment in a plant">
    <h3>Conveyors</h3>
    <p>Lorem ipsum dolor sit amet, consectetur adipiscing elit. Pellent esque dignissim eros a sapien tempus, ut eleifend neque convallis.</p>
    <a class="btn-ghost" href="#">LEARN MORE</a>
  </div>
</section>

<section class="news">
  <div class="news-copy">
    <p class="kicker">Whats going on</p>
    <h2 class="sec-title">Latest news &amp;<br>updates</h2>
    <p class="body-text">All the work completed was one man and one truck. As the company grew in versatility, it also grew physically. Harlan Welding Inc's shop was built in 1987 to accommodate the growth of the company, aiding in its ability in fabricating larger jobs.</p>
    <a class="btn" href="#">Learn More</a>
  </div>
  <article class="card c1">
    <div class="card-img" role="img" aria-label="Photo of a welded steel frame on a shop floor"></div>
    <h4>Industrial welding to the easiest fabrication</h4>
    <time>October 12, 2017</time>
    <a class="more" href="#">Read more</a>
  </article>
  <article class="card c2">
    <div class="card-img" role="img" aria-label="Photo of fabricated process piping inside a facility"></div>
    <h4>Fabricator with reputation of quality</h4>
    <time>October 11, 2017</time>
    <a class="more" href="#">Read more</a>
  </article>
</section>

<section class="about">
  <p class="kicker">About Us</p>
  <h2>We're committed to building a structure you can be proud of.</h2>
  <p class="lead">Our staff members are highly skilled and have years of experience and numerous professional certifications.<br>Quality is paramount and is embraced and appreciated by all of our staff.</p>
  <div class="pillars">
    <div class="pillar">
      <svg width="44" height="36" viewBox="0 0 44 36" fill="none" stroke="#222a30" stroke-width="2"><path d="M2 20c6-9 13-13 20-13s14 4 20 13c-6 9-13 13-20 13S8 29 2 20z"/><circle cx="22" cy="20" r="6"/><path d="M22 2v4M10 5l2 4M34 5l-2 4"/></svg>
      <h5>Our Vision</h5>
      <p>Lorem ipsum dolor sit amet, consectetur adipiscing elit. Pellent esque dignissim eros a sapien tempus, ut eleifend neque convallis.</p>
    </div>
    <div class="pillar">
      <svg width="44" height="36" viewBox="0 0 44 36" fill="none" stroke="#222a30" stroke-width="2"><path d="M22 2v6M8 32l14-22 14 22z"/><path d="M4 33h36"/></svg>
      <h5>Our Mission</h5>
      <p>Lorem ipsum dolor sit amet, consectetur adipiscing elit. Pellent esque dignissim eros a sapien tempus, ut eleifend neque convallis.</p>
    </div>
    <div class="pillar">
      <svg width="44" height="36" viewBox="0 0 44 36" fill="none" stroke="#222a30" stroke-width="2"><rect x="12" y="4" width="20" height="30" rx="2"/><path d="M18 2h8v5h-8zM16 15l2 2 3-3M24 16h5M16 24l2 2 3-3M24 25h5"/></svg>
      <h5>Our Experience</h5>
      <p>Lorem ipsum dolor sit amet, consectetur adipiscing elit. Pellent esque dignissim eros a sapien tempus, ut eleifend neque convallis.</p>
    </div>
  </div>
  <a class="btn" href="#">Learn More</a>
</section>

<section class="clients">
  <h2>Our Clients</h2>
  <p class="lead">Lorem ipsum dolor sit amet, consectetur adipiscing elit. Pellent esque dignissim eros a sapien tempus, ut eleifend neque convallis. Duis ac ligula nec sem fringilla. Mauris lacinia augue sagittis dolor.</p>
  <div class="logos">
    <div class="logo"><i></i>MarlowKibbleCo</div>
    <div class="logo">Dunholt University</div>
    <div class="logo">Tazzik</div>
    <div class="logo">Prairie Grains</div>
    <div class="logo">OKSU</div>
    <div class="logo"><i></i>FALSTO</div>
  </div>
</section>

<footer class="site-footer">
  <div class="wrap">
    <div class="foot-brand"><span class="brand-name">BRIVAN</span><span class="brand-sub">GROUP LTD</span></div>
    <div class="foot-social"><span></span><span></span><span></span></div>
    <ul class="foot-links fl1"><li>Home</li><li>About Us</li><li>Services</li><li>Why Us</li><li>Features</li><li>Blog</li><li>Contact Us</li></ul>
    <ul class="foot-links fl2"><li>Energy &amp; Utility Fabrication</li><li>Capabilities</li><li>Process Machinery</li><li>Facilities &amp; Equipment</li><li>Gallery</li></ul>
    <div class="foot-contact">
      <p>BRIVAN GROUP LTD</p>
      <p>Address will be appear here, some text will here, City, State, Country</p>
      <p>Call Me : +555 123 4567</p>
    </div>
    <div class="foot-bar">
      <span>Copyright 2017 All Rights Reserved by Brivan Group.</span>
      <nav><a href="#">Terms &amp; Conditions</a><a href="#">Privacy Policy</a></nav>
    </div>
  </div>
</footer>

</body>
</html>
```